Hair salon and Nail salon in Hawaii need a newspaper Ad design.

We need a newspaper Ad design for new open hair & nail salon in Waikiki Hawaii.Our Recommendation service for hair is "Head Spa" $30+tax and for nail is "Manicure Treatment Course" (Filing+Cuticle Care+Massage+Coloring) $20+tax.
We would like to see Hawaiian taste color and also having sense of luxury design. The ad size is W 5.0” x H 6.375”.
I would customers to know the shop place(Lanakila Crest Hotel 1F) , phone(808-555-0173), instagram(salonbrightwave) , our web site https://salonbrightwave.example and recommend services. For Web or Instagram , QR code is acceptable.

Target Market(s)

women & men

Industry/Entity Type

Beauty Salon

Font styles to use
Serif

Colors

Designer to choose colors to be used in the design.

Requirements
Must have
• Tagline for local customers. Shop Name is "SALON BRIGHTWAVE".the shop place(Lanakila Crest Hotel 1F) , phone(808-555-0173), instagram(salonbrightwave) and recommend services.
Nice to have
• Our services are competitive, but we don't want to be seen as just cheap and low quality.

```html
<!DOCTYPE html>
<html lang="en">
<head>
<meta charset="utf-8">
<title>Salon Brightwave – Newspaper Ad</title>
<link rel="stylesheet" href="https://fonts.googleapis.com/css2?family=Jost:ital,wght@0,300;0,400;0,700;1,300&family=Marcellus&display=swap">
<style>
  :root {
    --accent-red: #c62620;
    --ink: #161616;
    --marble-light: #f4f4f3;
    --marble-mid: #e6e6e5;
    --band: #000000;
    --band-text: #ffffff;
    --photo-warm: #b9a88d;
    --photo-glass: #d9d6cf;
    --photo-floor: #6f6a5e;
  }
  * { margin: 0; padding: 0; box-sizing: border-box; }
  html, body { width: 1200px; height: 941px; overflow: hidden; }
  body {
    position: relative;
    font-family: "Jost", sans-serif;
    color: var(--ink);
    background:
      linear-gradient(155deg, transparent 30%, rgba(200,200,200,0.25) 32%, transparent 36%),
      linear-gradient(25deg, transparent 55%, rgba(210,210,210,0.3) 57%, transparent 61%),
      radial-gradient(ellipse at 20% 30%, var(--marble-light), var(--marble-mid));
  }
  .brand {
    position: absolute; left: 63px; top: 78px;
    display: flex; align-items: center; gap: 16px;
  }
  .brand-mark { width: 50px; height: 51px; background: var(--ink); }
  .brand-name {
    font-family: "Marcellus", serif;
    font-size: 24px; letter-spacing: 0.5px; color: var(--ink);
  }
  .storefront-photo {
    position: absolute; left: 624px; top: 82px; width: 576px; height: 434px;
    z-index: 1;
    background:
      linear-gradient(90deg, var(--marble-light) 0%, rgba(244,244,243,0) 18%),
      linear-gradient(180deg, #b8b3a6 0%, #a8a396 20%, var(--photo-glass) 28%, var(--photo-warm) 60%, #8d6f55 75%, var(--photo-floor) 85%, #5b574d 100%);
  }
  .headline {
    position: absolute; left: 63px; top: 0; z-index: 2;
    color: var(--accent-red); font-weight: 300;
  }
  .headline span {
    position: absolute; left: 0; white-space: nowrap;
    font-size: 106px; line-height: 1; letter-spacing: -3px;
  }
  .headline .l1 { top: 176px; }
  .headline .l2 { top: 286px; }
  .headline .l3 { top: 396px; }
  .service { position: absolute; text-align: center; }
  .service-name { font-size: 60px; line-height: 1; font-weight: 400; white-space: nowrap; }
  .service-detail { font-size: 35px; font-style: italic; font-weight: 300; line-height: 1; margin-top: 10px; white-space: nowrap; }
  .service-price { color: var(--accent-red); font-weight: 700; font-size: 47px; line-height: 1; }
  .head-spa { left: 76px; top: 615px; width: 250px; }
  .head-spa .service-price { margin-top: 34px; }
  .manicure { left: 456px; top: 615px; width: 660px; }
  .manicure .service-name { font-size: 55px; letter-spacing: -0.5px; }
  .manicure .service-price { margin-top: 16px; }
  .contact-bar {
    position: absolute; left: 0; top: 857px; width: 1200px; height: 54px;
    background: var(--band); color: var(--band-text);
    font-family: "Jost", sans-serif; font-weight: 400; font-size: 23px; letter-spacing: 0.3px;
  }
  .contact-item {
    position: absolute; top: 0; height: 54px;
    display: flex; align-items: center; gap: 12px; white-space: nowrap;
  }
  .contact-item svg { display: block; }
  .c-place { left: 80px; }
  .c-phone { left: 423px; }
  .c-social { left: 633px; }
  .c-web { left: 862px; }
</style>
</head>
<body>
  <header class="brand">
    <div class="brand-mark"></div>
    <div class="brand-name">SALON BRIGHTWAVE</div>
  </header>

  <div class="storefront-photo" role="img" aria-label="Photo of the salon storefront with glass doors, red chairs and an easel menu board"></div>

  <h1 class="headline">
    <span class="l1">Are you ready</span>
    <span class="l2">for a new &amp;</span>
    <span class="l3">better you?</span>
  </h1>

  <section class="service head-spa">
    <h2 class="service-name">Head Spa</h2>
    <p class="service-price">$30+tax</p>
  </section>

  <section class="service manicure">
    <h2 class="service-name">Manicure Treatment Course</h2>
    <p class="service-detail">Filing + Cuticle Care + Massage + Coloring</p>
    <p class="service-price">$20+tax</p>
  </section>

  <footer class="contact-bar">
    <div class="contact-item c-place">
      <svg width="20" height="30" viewBox="0 0 20 30"><path d="M10 1a9 9 0 0 0-9 9c0 7 9 19 9 19s9-12 9-19a9 9 0 0 0-9-9z" fill="#fff"/><circle cx="10" cy="10" r="3.5" fill="#000"/></svg>
      <span>Lanakila Crest Hotel 1F</span>
    </div>
    <div class="contact-item c-phone">
      <svg width="20" height="34" viewBox="0 0 20 34"><rect x="1.5" y="1.5" width="17" height="31" rx="3" fill="none" stroke="#fff" stroke-width="3"/><rect x="7" y="27" width="6" height="2" fill="#fff"/></svg>
      <span>808-555-0173</span>
    </div>
    <div class="contact-item c-social">
      <svg width="24" height="24" viewBox="0 0 24 24"><circle cx="12" cy="12" r="10.5" fill="none" stroke="#fff" stroke-width="2.5"/></svg>
      <span>salonbrightwave</span>
    </div>
    <div class="contact-item c-web">
      <svg width="26" height="26" viewBox="0 0 26 26" fill="none" stroke="#fff" stroke-width="1.6"><circle cx="13" cy="13" r="11.5"/><ellipse cx="13" cy="13" rx="5" ry="11.5"/><path d="M1.5 13h23M3.5 7h19M3.5 19h19"/></svg>
      <span>salonbrightwave.example</span>
    </div>
  </footer>
</body>
</html>
```